Brightpath Coverage Partners
Stationary
Project: Brightpath Coverage Partners
Brightpath Coverage Partners -
Creative Brief
Professional
Dorian Fell
Agent / Broker
71362 West Maple Lane Ste. B Idyllwild, CA 92871-0517
dorian@brightpathcoverage.example
www.brightpathcoverage.example
Insurance License No: 0K72918
Please put the main lines of insurance I sell: Home, Auto, Commercial, Life, Health, Retirement

```html
<!DOCTYPE html>
<html lang="en">
<head>
<meta charset="utf-8">
<title>Brightpath Coverage Partners – Stationery</title>
<link href="https://fonts.googleapis.com/css2?family=Open+Sans:wght@400;600;700&display=swap" rel="stylesheet">
<style>
:root{
  --bg:#e7e4df;
  --paper:#ffffff;
  --navy:#1b2a6b;
  --blue:#2b43a8;
  --deep:#0c154f;
  --ink:#555a66;
  --rule:#c9ccd6;
  --faint:#e4e7f1;
}
*{box-sizing:border-box;margin:0;padding:0}
html,body{width:1200px;height:830px;overflow:hidden;background:var(--bg);font-family:"Open Sans",Arial,sans-serif;color:var(--ink)}
.canvas{position:relative;width:1200px;height:830px}
.piece{position:absolute;background:var(--paper);box-shadow:0 1px 4px rgba(0,0,0,.25);overflow:hidden}
.brand{display:flex;align-items:center;gap:3px;color:var(--navy);font-weight:600;line-height:1.05}
.brand i{display:block;width:7px;height:7px;background:var(--navy);flex:none}
.brand span{font-size:5px}
.brand.on-blue{color:#fff}.brand.on-blue i{background:#fff}
.addr{font-size:3.2px;line-height:1.45;color:var(--ink)}
.addr.light{color:#dfe4ff}
.mark{position:absolute;left:50%;transform:translateX(-50%);width:92px;height:92px;background:var(--faint);border-radius:4px}
.blueband{background:linear-gradient(100deg,var(--deep),var(--blue) 55%,var(--deep))}
/* business cards */
.card{position:absolute;width:78px;height:42px;background:var(--paper);box-shadow:0 1px 3px rgba(0,0,0,.3);padding:5px}
.card.dark{background:linear-gradient(120deg,var(--deep),var(--blue));}
.card .brand span{font-size:4px}.card .brand i{width:5px;height:5px}
.card .addr{font-size:2.6px;margin-top:4px}
.card.lg{width:92px;height:40px}
/* sheets */
.sheet{width:199px;height:290px;top:29px;padding:10px 12px}
.sheet .head{display:flex;justify-content:space-between;align-items:flex-start}
.sheet .head .addr{text-align:left;width:80px}
.title{font-size:6px;font-weight:700;color:var(--navy);text-align:center;margin:12px 0 5px}
.formrows{border-top:.6px solid var(--rule)}
.formrows div{display:flex;border-bottom:.6px solid var(--rule);height:9px;font-size:3.2px;align-items:center}
.formrows b{width:30px;font-weight:600;color:var(--navy)}
.checks{display:flex;gap:6px;font-size:3px;margin-top:5px}
.checks span::before{content:"";display:inline-block;width:3px;height:3px;border:.5px solid var(--ink);margin-right:1px}
table{border-collapse:collapse;width:100%;font-size:3px}
th{background:var(--navy);color:#fff;font-weight:600;padding:1.5px 2px;text-align:left}
td{border:.5px solid var(--rule);height:7px}
.foot{position:absolute;left:0;right:0;bottom:0;height:6px}
/* notepad */
.notepad{left:269px;top:355px;width:199px;height:437px;padding:12px}
.lines{margin-top:14px;background:repeating-linear-gradient(to bottom,transparent 0 10.5px,var(--rule) 10.5px 11.2px);height:390px}
/* envelopes */
.env{padding:8px}
.flap{position:absolute;left:0;right:0;top:0}
</style>
</head>
<body>
<div class="canvas">

  <!-- business cards, top set -->
  <div class="card" style="left:65px;top:96px"><div class="brand"><i></i><span>Brightpath Coverage Partners</span></div></div>
  <div class="card" style="left:150px;top:96px"><div class="addr" style="margin-top:2px">Dorian Fell<br>Agent / Broker<br>(951) 555-0142<br>dorian@brightpathcoverage.example</div></div>
  <div class="card" style="left:65px;top:148px"><div class="brand"><i></i><span>Brightpath Coverage Partners</span></div><div class="addr">Dorian Fell · Agent / Broker<br>www.brightpathcoverage.example</div></div>
  <div class="card dark" style="left:150px;top:148px"><div class="addr light">Home · Auto · Commercial<br>Life · Health · Retirement<br>Lic. No: 0K72918</div></div>
  <div class="card dark" style="left:65px;top:200px"><div class="brand on-blue"><i></i><span>Brightpath Coverage Partners</span></div></div>
  <div class="card dark" style="left:150px;top:200px"><div class="addr light">Dorian Fell<br>Agent / Broker<br>(951) 555-0142</div></div>
  <div class="card dark" style="left:65px;top:252px"><div class="brand on-blue"><i></i><span>Brightpath Coverage Partners</span></div><div class="addr light">Insurance License No: 0K72918</div></div>
  <div class="card" style="left:150px;top:252px"><div class="addr">71362 West Maple Lane Ste. B<br>Idyllwild, CA 92871-0517<br>www.brightpathcoverage.example</div></div>

  <!-- fax cover -->
  <div class="piece sheet" style="left:269px">
    <div class="head">
      <div class="brand"><i></i><span>Brightpath Coverage<br>Partners</span></div>
      <div class="addr">71362 West Maple Lane Ste. B<br>Idyllwild, CA 92871-0517<br>P (951) 555-0142<br>F (951) 555-0199<br>www.brightpathcoverage.example</div>
    </div>
    <div class="title">FAX COVER</div>
    <div class="formrows">
      <div><b>To:</b></div><div><b>Fax:</b></div><div><b>Phone:</b></div><div><b>Re:</b></div><div><b>From:</b></div><div><b>Date:</b></div>
    </div>
    <div class="checks"><span>Urgent</span><span>For Review</span><span>Please Reply</span><span>Comment</span></div>
    <div class="mark" style="top:170px"></div>
  </div>

  <!-- letterhead -->
  <div class="piece sheet" style="left:492px">
    <div class="head">
      <div class="brand"><i></i><span>Brightpath Coverage<br>Partners</span></div>
      <div class="addr">71362 West Maple Lane Ste. B<br>Idyllwild, CA 92871-0517<br>P (951) 555-0142<br>dorian@brightpathcoverage.example<br>www.brightpathcoverage.example</div>
    </div>
    <div class="mark" style="top:120px;width:110px;height:110px"></div>
  </div>

  <!-- invoice forms -->
  <div class="piece sheet" style="left:713px">
    <div class="head">
      <div class="brand"><i></i><span>Brightpath Coverage<br>Partners</span></div>
      <div class="addr">71362 West Maple Lane Ste. B<br>Idyllwild, CA 92871-0517<br>P (951) 555-0142</div>
    </div>
    <table style="margin-top:10px"><tr><th>Bill To</th><th>Invoice No</th><th>Date</th></tr><tr><td></td><td></td><td></td></tr><tr><td></td><td></td><td></td></tr></table>
    <table style="margin-top:6px"><tr><th>Item</th><th>Description</th><th>Qty</th><th>Amount</th></tr>
      <tr><td></td><td></td><td></td><td></td></tr><tr><td></td><td></td><td></td><td></td></tr><tr><td></td><td></td><td></td><td></td></tr><tr><td></td><td></td><td></td><td></td></tr><tr><td></td><td></td><td></td><td></td></tr><tr><td></td><td></td><td></td><td></td></tr></table>
    <div class="mark" style="top:140px"></div>
  </div>
  <div class="piece sheet" style="left:931px">
    <div class="head">
      <div class="brand"><i></i><span>Brightpath Coverage<br>Partners</span></div>
      <div class="addr">71362 West Maple Lane Ste. B<br>Idyllwild, CA 92871-0517<br>P (951) 555-0142</div>
    </div>
    <table style="margin-top:10px"><tr><th>Customer</th><th>Policy No</th><th>Due</th></tr><tr><td></td><td></td><td></td></tr></table>
    <table style="margin-top:6px"><tr><th>Coverage</th><th>Description</th><th>Rate</th><th>Total</th></tr>
      <tr><td></td><td></td><td></td><td></td></tr><tr><td></td><td></td><td></td><td></td></tr><tr><td></td><td></td><td></td><td></td></tr><tr><td></td><td></td><td></td><td></td></tr></table>
    <div class="mark" style="top:140px"></div>
  </div>

  <!-- envelope left -->
  <div class="piece env" style="left:29px;top:384px;width:223px;height:96px">
    <div class="brand"><i></i><span>Brightpath Coverage<br>Partners</span></div>
    <div class="addr" style="margin-top:3px">71362 West Maple Lane Ste. B<br>Idyllwild, CA 92871-0517</div>
  </div>
  <div class="piece" style="left:29px;top:486px;width:223px;height:114px">
    <svg class="flap" width="223" height="60" viewBox="0 0 223 60"><defs><linearGradient id="fl" x1="0" x2="1"><stop offset="0" stop-color="#0c154f"/><stop offset=".5" stop-color="#2b43a8"/><stop offset="1" stop-color="#0c154f"/></linearGradient></defs><path d="M0 0H223V22Q111 60 0 22Z" fill="url(#fl)"/></svg>
    <div class="brand on-blue" style="position:absolute;left:80px;top:10px"><i></i><span>Brightpath Coverage Partners</span></div>
  </div>

  <!-- business cards, bottom set -->
  <div class="card lg" style="left:43px;top:619px"><div class="brand"><i></i><span>Brightpath Coverage Partners</span></div></div>
  <div class="card lg" style="left:145px;top:619px"><div class="addr">Dorian Fell · Agent / Broker<br>(951) 555-0142<br>dorian@brightpathcoverage.example</div></div>
  <div class="card lg" style="left:43px;top:665px"><div class="brand"><i></i><span>Brightpath Coverage Partners</span></div><div class="addr">www.brightpathcoverage.example</div></div>
  <div class="card lg dark" style="left:145px;top:665px"><div class="addr light">Home · Auto · Commercial<br>Life · Health · Retirement</div></div>
  <div class="card lg" style="left:43px;top:711px"><div class="addr">71362 West Maple Lane Ste. B<br>Idyllwild, CA 92871-0517</div></div>
  <div class="card lg dark" style="left:145px;top:711px"><div class="brand on-blue"><i></i><span>Brightpath Coverage Partners</span></div></div>
  <div class="card lg" style="left:43px;top:757px"><div class="brand"><i></i><span>Brightpath Coverage Partners</span></div></div>
  <div class="card lg" style="left:145px;top:757px"><div class="addr">Insurance License No: 0K72918<br>Dorian Fell</div></div>

  <!-- notepad -->
  <div class="piece notepad">
    <div class="brand"><i></i><span>Brightpath Coverage Partners</span></div>
    <div class="lines"></div>
  </div>

  <!-- presentation folder -->
  <div class="piece blueband" style="left:492px;top:348px;width:208px;height:352px;box-shadow:none">
    <div class="mark" style="top:90px;width:110px;height:110px;background:rgba(255,255,255,.12)"></div>
    <div class="addr light" style="position:absolute;left:14px;bottom:22px">71362 West Maple Lane Ste. B<br>Idyllwild, CA 92871-0517<br>P (951) 555-0142<br>dorian@brightpathcoverage.example<br>www.brightpathcoverage.example</div>
  </div>
  <div class="piece" style="left:700px;top:348px;width:207px;height:352px;box-shadow:none;padding:14px">
    <div class="brand" style="justify-content:center"><i></i><span>Brightpath Coverage Partners</span></div>
    <div class="mark" style="top:70px;width:120px;height:120px"></div>
  </div>
  <svg style="position:absolute;left:492px;top:700px" width="415" height="104" viewBox="0 0 415 104">
    <path d="M0 0H208V104H30L0 60Z" fill="#fff"/>
    <path d="M208 0H415V60L385 104H236L208 60Z" fill="#fff"/>
    <path d="M208 0V104M0 0H415" stroke="#c9ccd6" stroke-width=".8" fill="none"/>
  </svg>

  <!-- envelopes right -->
  <div class="piece env" style="left:936px;top:348px;width:240px;height:100px">
    <div class="brand"><i></i><span>Brightpath Coverage<br>Partners</span></div>
    <div class="addr" style="margin-top:3px">71362 West Maple Lane Ste. B<br>Idyllwild, CA 92871-0517<br>www.brightpathcoverage.example</div>
  </div>
  <div class="piece" style="left:936px;top:455px;width:240px;height:105px">
    <svg class="flap" width="240" height="105" viewBox="0 0 240 105"><path d="M0 0L120 52L240 0" fill="none" stroke="#c9ccd6" stroke-width=".8"/><path d="M0 105L100 45M240 105L140 45" stroke="#dde0e8" stroke-width=".8"/></svg>
  </div>
  <div class="piece blueband" style="left:936px;top:590px;width:240px;height:110px">
    <svg class="flap" width="240" height="110" viewBox="0 0 240 110"><path d="M0 0L120 60L240 0" fill="none" stroke="rgba(255,255,255,.35)" stroke-width=".8"/></svg>
    <div class="brand on-blue" style="position:absolute;left:70px;bottom:16px"><i></i><span>Brightpath Coverage Partners</span></div>
  </div>
  <div class="piece env" style="left:936px;top:704px;width:240px;height:100px">
    <div class="brand"><i></i><span>Brightpath Coverage<br>Partners</span></div>
    <div class="addr" style="margin-top:3px">71362 West Maple Lane Ste. B<br>Idyllwild, CA 92871-0517</div>
    <div class="foot blueband"></div>
  </div>

</div>
</body>
</html>
```